Business Card and Letterhead for Vantage Psychology

We need a business card design and letterhead to use for our Psychology firm that specializes in psychoeducational assessments and individual therapy. Our motto is Purpose-Driven Assessments, Meaning-Centered Therapy.Our contact information is as follows:
Vantage Psychology
The Marwick Block - 6127-48St.
Box 2716 Ashvale, WR
T2K 3M8
t 403.555.0148 (VANT)
f 403.555.0172
www.vantagepsychology-example.ca
The business card will be used for two different psychologists so I can supply names nearer to completion. We prefer clean, uncluttered looks.

Target Market(s)

Clients, Educators

Font styles to use
Sans Serif

Colors

Designer to choose colors to be used in the design.

Requirements
Must have
• All relevant contact info, logo, some "white" space.
Nice to have
• It would be nice to see letterhead options that have the logo on the top of the page but also options that have it on the side. I think top of the page is probably our preference.
Should not have
• Too much clutter!

```html
<!DOCTYPE html>
<html lang="en">
<head>
<meta charset="utf-8">
<title>Vantage Psychology – Business Card</title>
<link rel="stylesheet" href="https://fonts.googleapis.com/css2?family=Orbitron:wght@500;600&family=Poppins:wght@400&display=swap">
<style>
  :root {
    --stage: #232122;
    --card-blue: #56bddb;
    --logo-blue: #4fb6d6;
    --accent-orange: #f5a03f;
    --white: #ffffff;
    --pattern-blue: #e3f3f9;
    --pattern-peach: #fdf0e3;
  }
  html, body {
    margin: 0;
    width: 1125px;
    height: 1200px;
    overflow: hidden;
    background: var(--stage);
  }
  .card {
    position: absolute;
    left: 166px;
    width: 800px;
    height: 456px;
    border-radius: 26px;
    overflow: hidden;
  }
  .card-front { top: 103px; background: var(--card-blue); }
  .card-back { top: 619px; background: var(--white); }

  .contact {
    position: absolute;
    left: 43px;
    top: 96px;
    color: var(--white);
    font-family: "Poppins", sans-serif;
    font-size: 17px;
    line-height: 22.5px;
  }
  .contact-name {
    margin: 0;
    font-family: "Orbitron", sans-serif;
    font-weight: 600;
    font-size: 25px;
    letter-spacing: 1px;
    line-height: 30px;
  }
  .contact-role { margin: 6px 0 25px; }
  .contact-address { margin: 0 0 9px; font-style: normal; }
  .contact-lines { margin: 0; line-height: 26px; }

  .brand-panel {
    position: absolute;
    left: 390px;
    top: 48px;
    width: 390px;
    height: 390px;
    border-radius: 50%;
    background: var(--white);
  }
  .brand-dot {
    position: absolute;
    left: 146px;
    top: 136px;
    width: 98px;
    height: 98px;
    border-radius: 50%;
    background: var(--logo-blue);
  }
  .brand-name {
    position: absolute;
    left: 0;
    right: 0;
    top: 238px;
    margin: 0;
    text-align: center;
    font-family: "Orbitron", sans-serif;
    font-weight: 500;
    font-size: 20px;
    letter-spacing: 0.5px;
    color: var(--logo-blue);
  }

  .back-pattern {
    position: absolute;
    inset: 0;
    background: linear-gradient(135deg, var(--pattern-blue), var(--pattern-peach) 50%, var(--pattern-blue));
  }
  .back-dot {
    position: absolute;
    left: 655px;
    top: 336px;
    width: 54px;
    height: 54px;
    border-radius: 50%;
    background: var(--logo-blue);
  }
</style>
</head>
<body>
  <section class="card card-front">
    <div class="contact">
      <h1 class="contact-name">DANIEL HARPER</h1>
      <p class="contact-role">President</p>
      <address class="contact-address">The Marwick<br>Block - 6127-48St.<br>Box 2716 Ashvale, WR<br>T2K 3M8</address>
      <p class="contact-lines">P. 403.555.0148 (VANT)<br>F. 403.555.0172<br>www.vantagepsychology-example.ca</p>
    </div>
    <div class="brand-panel">
      <div class="brand-dot"></div>
      <p class="brand-name">VANTAGE PSYCHOLOGY</p>
    </div>
  </section>

  <section class="card card-back">
    <div class="back-pattern" role="img" aria-label="Repeating soft pattern of the practice emblem in pale blue and peach"></div>
    <div class="back-dot"></div>
  </section>
</body>
</html>
```